Powerpoint design for Summit Lane Advisors

We would like to have a Power point template/design with flexibilities and good opportunities to do changes.
• Be able to change in image background
• Themes are SLA colors and complementary colors. Please come with suggestions.
• Alternate white and blue background
• Standard functions and opportunities within Powerpoint should be able to be used or be accessible.
• Feel free to change/alter the logo for example remove or separate the text in the logo ("Summit Lane Advisors" ) and the tagline ("Clear advice, lasting results")
• www.summitlaneadvisors.se

```html
<!DOCTYPE html>
<html lang="en">
<head>
<meta charset="utf-8">
<title>Summit Lane Advisors – Presentation Template</title>
<link href="https://fonts.googleapis.com/css2?family=Libre+Baskerville:wght@400;700&family=Open+Sans:wght@400;600;700;800&display=swap" rel="stylesheet">
<style>
:root{
  --navy:#0f3a78;
  --blue:#1f5aa6;
  --sky:#6f93c8;
  --ink:#3a3f47;
  --grey:#8a9099;
  --rule:#dfe3e8;
  --mist:#f1f3f6;
  --red:#9c1b1b;
  --white:#ffffff;
  --stage:#eef0f3;
}
*{box-sizing:border-box;margin:0;padding:0}
html,body{width:1200px;height:4580px;overflow:hidden;background:var(--white)}
body{position:relative;font-family:"Open Sans",Arial,sans-serif;color:var(--ink)}
.stage{position:absolute;left:0;top:0;width:1200px;height:1180px;background:var(--stage)}
.thumb{position:absolute;transform-origin:0 0}
.slide{position:absolute;width:553px;height:311px;overflow:hidden;background:var(--white);box-shadow:0 3px 12px rgba(15,40,80,.14)}
.slide.navy{background:var(--navy);color:var(--white)}
.serif{font-family:"Libre Baskerville",Georgia,serif}
.bar{position:absolute;left:0;top:14px;width:3px;height:24px;background:var(--navy)}
.s-title{position:absolute;left:22px;top:14px;font:400 18px "Libre Baskerville",Georgia,serif;color:var(--navy)}
.s-sub{position:absolute;left:22px;top:38px;font-size:7px;color:var(--grey)}
.navy .s-title,.navy .s-sub{color:var(--white)}
.mark{position:absolute;right:14px;top:12px;font:800 20px "Open Sans",Arial,sans-serif;color:var(--navy);letter-spacing:-.5px}
.navy .mark{color:var(--white)}
.foot{position:absolute;left:22px;bottom:8px;font-size:5px;color:var(--grey)}
.page{position:absolute;right:22px;bottom:8px;font-size:5px;color:var(--grey)}
.navy .foot,.navy .page{color:#c9d6ea}
.txt{font-size:5.5px;line-height:1.55;color:var(--grey)}
.navy .txt{color:#dbe4f2}
.h-small{font:700 6px "Libre Baskerville",Georgia,serif;color:var(--navy);margin-bottom:3px}
.ghost{position:absolute;font:800 180px "Open Sans",Arial,sans-serif;color:rgba(15,58,120,.045);letter-spacing:-6px;line-height:1}
.ph{position:absolute}
.brand{font:700 15px "Open Sans",Arial,sans-serif;color:var(--navy)}
.tag{font-size:8px;letter-spacing:2px;color:var(--blue)}
.socials{position:absolute;display:flex;gap:3px}
.socials i{display:block;width:8px;height:8px;border:1px solid currentColor;border-radius:50%}
.vurl{position:absolute;right:14px;top:40px;writing-mode:vertical-rl;font-size:5px;color:var(--grey);letter-spacing:.5px}
.btn{display:inline-block;background:var(--blue);color:var(--white);font-size:5.5px;padding:4px 10px;border-radius:8px}
.list-row{border-bottom:1px solid var(--rule);font-size:6px;padding:6px 0 5px;color:var(--ink)}
.toc-num{font:700 32px "Libre Baskerville",Georgia,serif;color:#d7dbe1;line-height:1}
.member{position:absolute;top:60px;width:105px}
.member .photo{height:80px}
.member .name{background:var(--navy);color:var(--white);font:400 6px "Libre Baskerville",Georgia,serif;text-align:center;padding:3px 0}
.member .txt{text-align:center;margin-top:5px}
.member .socials{position:static;justify-content:center;margin-top:4px;color:var(--navy)}
.contact-row{display:flex;align-items:center;gap:8px;font-size:5.5px;color:var(--grey);margin-bottom:7px}
</style>
</head>
<body>

<section class="stage" aria-label="Featured slides">

  <div class="thumb" style="left:30px;top:50px;transform:scale(.651)">
    <div class="slide">
      <div class="ph" role="img" aria-label="Strip collage of business photos: coffee desk, charts, technology" style="left:0;top:0;width:553px;height:218px;background:linear-gradient(90deg,#b07a3e 0%,#d8c1a0 25%,#c9cfd6 45%,#3b4048 65%,#1b2430 85%,#5c636c 100%)"></div>
      <div style="position:absolute;left:0;top:218px;width:553px;height:93px;background:var(--mist)"></div>
      <span class="mark" style="left:36px;right:auto;top:246px;font-size:24px">SLA</span>
      <div style="position:absolute;left:140px;top:240px;width:1px;height:40px;background:var(--sky)"></div>
      <p class="serif" style="position:absolute;left:160px;top:246px;font-size:15px;color:var(--navy)">Summit Lane Advisors Template</p>
      <p style="position:absolute;left:160px;top:270px;font-size:6px;color:var(--grey)">Month 2021</p>
    </div>
  </div>

  <div class="thumb" style="left:420px;top:50px;transform:scale(.651)">
    <div class="slide">
      <div class="bar"></div><h2 class="s-title">Agenda</h2>
      <div class="ph" role="img" aria-label="Portrait photo of a smiling businessman with arms crossed" style="left:40px;top:100px;width:110px;height:211px;background:linear-gradient(180deg,#c9cdd2,#6b7a90)"></div>
      <p style="position:absolute;left:120px;top:140px;font:800 70px 'Open Sans',Arial,sans-serif;color:var(--navy)">SLA</p>
      <div style="position:absolute;left:318px;top:35px;width:210px">
        <div class="list-row">1. Introduction</div><div class="list-row">2. About Us</div><div class="list-row">3. Welcome Message</div><div class="list-row">4. Our Services</div><div class="list-row">5. Our Team</div><div class="list-row">6. Contact Us</div>
      </div>
    </div>
  </div>

  <div class="thumb" style="left:810px;top:50px;transform:scale(.651)">
    <div class="slide">
      <div class="bar"></div><h2 class="s-title">Timeline</h2><p class="s-sub">Subtitle Goes Here</p><span class="mark">SLA</span>
      <svg style="position:absolute;left:0;top:0" width="553" height="311" viewBox="0 0 553 311">
        <text x="30" y="152" font-size="9" fill="#3a3f47" font-family="Open Sans">Start</text>
        <text x="30" y="162" font-size="5" fill="#8a9099" font-family="Open Sans">Contents</text>
        <line x1="30" y1="155" x2="470" y2="155" stroke="#b8c4d6" stroke-width="1.5"/>
        <g fill="#8a9099" font-size="5" font-family="Open Sans" text-anchor="middle">
          <circle cx="130" cy="155" r="9" fill="#a9c1e2"/><text x="130" y="140">2013</text>
          <circle cx="185" cy="155" r="9" fill="#6f93c8"/><text x="185" y="175">2014</text>
          <circle cx="240" cy="155" r="9" fill="#3e6fb0"/><text x="240" y="140">2016</text>
          <circle cx="295" cy="155" r="9" fill="#1f5aa6"/><text x="295" y="175">2018</text>
          <circle cx="350" cy="155" r="9" fill="#163f7a"/><text x="350" y="140">2019</text>
          <circle cx="405" cy="155" r="9" fill="#0f2a55"/><text x="405" y="175">2020</text>
        </g>
        <circle cx="470" cy="155" r="19" fill="#9c1b1b"/>
        <text x="470" y="158" font-size="9" fill="#fff" text-anchor="middle" font-family="Open Sans" font-weight="700">2021</text>
        <text x="470" y="126" font-size="8" fill="#9c1b1b" text-anchor="middle" font-family="Open Sans" font-weight="700">Vision</text>
      </svg>
      <p class="foot">© Copyright Summit Lane Advisors | All Rights Reserved</p><p class="page">PAGE | 10</p>
    </div>
  </div>

  <div class="thumb" style="left:30px;top:300px;transform:scale(.651)">
    <div class="slide navy">
      <h2 class="s-title">Your Title Here</h2><p class="s-sub">Subtitle Goes Here</p><span class="mark">SLA</span>
      <div style="position:absolute;left:22px;top:110px;width:220px">
        <p class="h-small" style="color:#fff">Content Here</p>
        <p class="txt">You can simply impress your audience and add a unique touch to your presentations. Easy to change colours, photos and text. A clean, modern layout that is easy to edit with your own colours and photos, built to look polished.</p>
        <p style="margin-top:10px"><span class="btn">Learn More</span></p>
      </div>
      <div class="ph" role="img" aria-label="Laptop on a desk with a coffee cup" style="left:300px;top:100px;width:230px;height:140px;background:linear-gradient(135deg,#f4f6f9,#c9cfd8 60%,#8b96a6)"></div>
      <p class="foot">© Copyright Summit Lane Advisors | All Rights Reserved</p><p class="page">PAGE | 9</p>
    </div>
  </div>

  <div class="thumb" style="left:420px;top:300px;transform:scale(.651)">
    <div class="slide">
      <div class="bar"></div><h2 class="s-title">Your Title Here</h2><p class="s-sub">Subtitle Goes Here</p><span class="mark">SLA</span>
      <div class="ghost" style="left:270px;top:70px;font-size:120px">SLA</div>
      <div style="position:absolute;left:42px;top:90px;width:200px">
        <p class="h-small" style="text-align:center">Content Here</p>
        <p class="txt">You can simply impress your audience and add a unique touch to your presentations. Easy to change colours, photos and text. A clean, modern layout that is easy to edit with your own colours and photos.</p>
      </div>
      <p class="foot">© Copyright Summit Lane Advisors | All Rights Reserved</p><p class="page">PAGE | 8</p>
    </div>
  </div>

  <div class="thumb" style="left:810px;top:300px;transform:scale(.651)">
    <div class="slide">
      <div class="bar"></div><h2 class="s-title">Table Of Content</h2><span class="mark">SLA</span>
      <div style="position:absolute;left:22px;top:75px;display:grid;grid-template-columns:230px 230px;row-gap:18px;column-gap:20px">
        <div style="display:flex;gap:8px"><span class="toc-num">1</span><div><p class="h-small">Content here</p><p class="txt">Easy to edit with your own colours and photos.</p></div></div>
        <div style="display:flex;gap:8px"><span class="toc-num">4</span><div><p class="h-small">Content here</p><p class="txt">Easy to edit with your own colours and photos.</p></div></div>
        <div style="display:flex;gap:8px"><span class="toc-num">2</span><div><p class="h-small">Content here</p><p class="txt">Easy to edit with your own colours and photos.</p></div></div>
        <div style="display:flex;gap:8px"><span class="toc-num">5</span><div><p class="h-small">Content here</p><p class="txt">Easy to edit with your own colours and photos.</p></div></div>
        <div style="display:flex;gap:8px"><span class="toc-num">3</span><div><p class="h-small">Content here</p><p class="txt">Easy to edit with your own colours and photos.</p></div></div>
        <div style="display:flex;gap:8px"><span class="toc-num">6</span><div><p class="h-small">Content here</p><p class="txt">Easy to edit with your own colours and photos.</p></div></div>
      </div>
      <p class="foot">© Copyright Summit Lane Advisors | All Rights Reserved</p><p class="page">PAGE | 7</p>
    </div>
  </div>

  <div class="thumb" style="left:210px;top:570px;transform:scale(1.41)">
    <div class="slide">
      <div class="ghost" style="left:-10px;top:60px">SLA</div>
      <div style="position:absolute;left:0;top:95px;width:553px;text-align:center">
        <p style="font:800 44px 'Open Sans',Arial,sans-serif;color:var(--navy);line-height:1">SLA</p>
        <p class="brand" style="margin-top:4px">Summit Lane Advisors</p>
        <p class="tag">Clear advice, lasting results</p>
      </div>
      <p class="vurl">www.summitlaneadvisors.se</p>
    </div>
  </div>
</section>

<div class="slide" style="left:30px;top:1223px">
  <div class="ghost" style="left:-10px;top:60px">SLA</div>
  <div style="position:absolute;left:0;top:95px;width:553px;text-align:center">
    <p style="font:800 44px 'Open Sans',Arial,sans-serif;color:var(--navy);line-height:1">SLA</p>
    <p class="brand" style="margin-top:4px">Summit Lane Advisors</p>
    <p class="tag">Clear advice, lasting results</p>
  </div>
  <p class="vurl">www.summitlaneadvisors.se</p>
</div>

<div class="slide" style="left:617px;top:1223px">
  <p style="position:absolute;left:50px;top:110px;font:800 70px 'Open Sans',Arial,sans-serif;color:var(--navy);line-height:1">SLA</p>
  <div style="position:absolute;left:278px;top:25px;width:1px;height:260px;background:var(--rule)"></div>
  <div style="position:absolute;left:330px;top:45px;width:30px;height:1.5px;background:var(--navy)"></div>
  <p class="serif" style="position:absolute;left:330px;top:52px;font-size:22px;line-height:1.2;color:var(--navy)">Master Slide<br>Presentation</p>
  <p style="position:absolute;left:330px;top:110px;font-size:6px;color:var(--grey)">Subtitle Goes Here</p>
  <div class="socials" style="left:330px;top:262px;color:var(--navy)"><i></i><i></i><i></i><i></i></div>
</div>

<div class="slide navy" style="left:30px;top:1559px">
  <p style="position:absolute;left:50px;top:110px;font:800 70px 'Open Sans',Arial,sans-serif;color:var(--white);line-height:1">SLA</p>
  <div style="position:absolute;left:278px;top:25px;width:1px;height:260px;background:rgba(255,255,255,.35)"></div>
  <div style="position:absolute;left:330px;top:45px;width:30px;height:1.5px;background:var(--white)"></div>
  <p class="serif" style="position:absolute;left:330px;top:52px;font-size:22px;line-height:1.2">Master Slide<br>Presentation</p>
  <p style="position:absolute;left:330px;top:110px;font-size:6px">Subtitle Goes Here</p>
  <div class="socials" style="left:330px;top:262px;color:var(--white)"><i></i><i></i><i></i><i></i></div>
</div>

<div class="slide" style="left:617px;top:1559px">
  <p style="position:absolute;left:0;top:8px;width:553px;text-align:center;font:800 24px 'Open Sans',Arial,sans-serif;color:var(--navy)">SLA</p>
  <div class="ph" role="img" aria-label="Blue-toned photo of a hand writing on documents at a desk" style="left:0;top:65px;width:553px;height:246px;background:linear-gradient(180deg,#2d5b97,#1a4684 60%,#274f85)"></div>
  <div style="position:absolute;left:0;top:90px;width:553px;text-align:center;color:var(--white)">
    <p style="font-size:6px;letter-spacing:1.5px">www.summitlaneadvisors.se</p>
    <p class="serif" style="font-size:19px;margin-top:22px">SLA Master Slide Template</p>
    <p style="font-size:5.5px;letter-spacing:3px;margin-top:5px">SUBTITLE GOES HERE</p>
    <p style="font-size:5.5px;margin-top:22px">Month 2021</p>
  </div>
  <div class="socials" style="left:256px;top:278px;color:var(--white)"><i></i><i></i><i></i><i></i></div>
</div>

<div class="slide" style="left:30px;top:1893px">
  <div class="ph" role="img" aria-label="Strip collage of business photos: coffee desk, charts, technology" style="left:0;top:0;width:553px;height:218px;background:linear-gradient(90deg,#b07a3e 0%,#d8c1a0 25%,#c9cfd6 45%,#3b4048 65%,#1b2430 85%,#5c636c 100%)"></div>
  <div style="position:absolute;left:0;top:218px;width:553px;height:93px;background:var(--mist)"></div>
  <span class="mark" style="left:36px;right:auto;top:246px;font-size:24px">SLA</span>
  <div style="position:absolute;left:140px;top:240px;width:1px;height:40px;background:var(--sky)"></div>
  <p class="serif" style="position:absolute;left:160px;top:246px;font-size:15px;color:var(--navy)">Summit Lane Advisors Template</p>
  <p style="position:absolute;left:160px;top:270px;font-size:6px;color:var(--grey)">Month 2021</p>
</div>

<div class="slide" style="left:617px;top:1893px">
  <div class="bar"></div><h2 class="s-title">Agenda</h2>
  <div class="ph" role="img" aria-label="Portrait photo of a smiling businessman with arms crossed" style="left:40px;top:100px;width:110px;height:211px;background:linear-gradient(180deg,#c9cdd2,#6b7a90)"></div>
  <p style="position:absolute;left:120px;top:140px;font:800 70px 'Open Sans',Arial,sans-serif;color:var(--navy)">SLA</p>
  <div style="position:absolute;left:318px;top:35px;width:210px">
    <div class="list-row">1. Introduction</div><div class="list-row">2. About Us</div><div class="list-row">3. Welcome Message</div><div class="list-row">4. Our Services</div><div class="list-row">5. Our Team</div><div class="list-row">6. Contact Us</div>
  </div>
</div>

<div class="slide" style="left:30px;top:2228px">
  <div class="bar"></div><h2 class="s-title">Table Of Content</h2><span class="mark">SLA</span>
  <div style="position:absolute;left:22px;top:75px;display:grid;grid-template-columns:230px 230px;row-gap:18px;column-gap:20px">
    <div style="display:flex;gap:8px"><span class="toc-num">1</span><div><p class="h-small">Content here</p><p class="txt">Easy to edit with your own colours and photos.</p></div></div>
    <div style="display:flex;gap:8px"><span class="toc-num">4</span><div><p class="h-small">Content here</p><p class="txt">Easy to edit with your own colours and photos.</p></div></div>
    <div style="display:flex;gap:8px"><span class="toc-num">2</span><div><p class="h-small">Content here</p><p class="txt">Easy to edit with your own colours and photos.</p></div></div>
    <div style="display:flex;gap:8px"><span class="toc-num">5</span><div><p class="h-small">Content here</p><p class="txt">Easy to edit with your own colours and photos.</p></div></div>
    <div style="display:flex;gap:8px"><span class="toc-num">3</span><div><p class="h-small">Content here</p><p class="txt">Easy to edit with your own colours and photos.</p></div></div>
    <div style="display:flex;gap:8px"><span class="toc-num">6</span><div><p class="h-small">Content here</p><p class="txt">Easy to edit with your own colours and photos.</p></div></div>
  </div>
  <p class="foot">© Copyright Summit Lane Advisors | All Rights Reserved</p><p class="page">PAGE | 7</p>
</div>

<div class="slide" style="left:617px;top:2228px">
  <div class="bar"></div><h2 class="s-title">Your Title Here</h2><p class="s-sub">Subtitle Goes Here</p><span class="mark">SLA</span>
  <div class="ghost" style="left:270px;top:70px;font-size:120px">SLA</div>
  <div style="position:absolute;left:42px;top:90px;width:200px">
    <p class="h-small" style="text-align:center">Content Here</p>
    <p class="txt">You can simply impress your audience and add a unique touch to your presentations. Easy to change colours, photos and text. A clean, modern layout that is easy to edit with your own colours and photos.</p>
  </div>
  <p class="foot">© Copyright Summit Lane Advisors | All Rights Reserved</p><p class="page">PAGE | 8</p>
</div>

<div class="slide navy" style="left:30px;top:2562px">
  <h2 class="s-title">Your Title Here</h2><p class="s-sub">Subtitle Goes Here</p><span class="mark">SLA</span>
  <div style="position:absolute;left:22px;top:110px;width:220px">
    <p class="h-small" style="color:#fff">Content Here</p>
    <p class="txt">You can simply impress your audience and add a unique touch to your presentations. Easy to change colours, photos and text. A clean, modern layout that is easy to edit with your own colours and photos, built to look polished.</p>
    <p style="margin-top:10px"><span class="btn">Learn More</span></p>
  </div>
  <div class="ph" role="img" aria-label="Laptop on a desk with a coffee cup" style="left:300px;top:100px;width:230px;height:140px;background:linear-gradient(135deg,#f4f6f9,#c9cfd8 60%,#8b96a6)"></div>
  <p class="foot">© Copyright Summit Lane Advisors | All Rights Reserved</p><p class="page">PAGE | 9</p>
</div>

<div class="slide" style="left:617px;top:2562px">
  <div class="bar"></div><h2 class="s-title">Timeline</h2><p class="s-sub">Subtitle Goes Here</p><span class="mark">SLA</span>
  <svg style="position:absolute;left:0;top:0" width="553" height="311" viewBox="0 0 553 311">
    <text x="30" y="152" font-size="9" fill="#3a3f47" font-family="Open Sans">Start</text>
    <text x="30" y="162" font-size="5" fill="#8a9099" font-family="Open Sans">Contents</text>
    <line x1="30" y1="155" x2="470" y2="155" stroke="#b8c4d6" stroke-width="1.5"/>
    <g fill="#8a9099" font-size="5" font-family="Open Sans" text-anchor="middle">
      <circle cx="130" cy="155" r="9" fill="#a9c1e2"/><text x="130" y="140">2013</text><text x="130" y="200">Easy to edit</text><text x="130" y="207">with your text</text>
      <circle cx="185" cy="155" r="9" fill="#6f93c8"/><text x="185" y="175">2014</text><text x="185" y="100">Easy to edit</text><text x="185" y="107">with your text</text>
      <circle cx="240" cy="155" r="9" fill="#3e6fb0"/><text x="240" y="140">2016</text><text x="240" y="200">Easy to edit</text><text x="240" y="207">with your text</text>
      <circle cx="295" cy="155" r="9" fill="#1f5aa6"/><text x="295" y="175">2018</text><text x="295" y="100">Easy to edit</text><text x="295" y="107">with your text</text>
      <circle cx="350" cy="155" r="9" fill="#163f7a"/><text x="350" y="140">2019</text><text x="350" y="200">Easy to edit</text><text x="350" y="207">with your text</text>
      <circle cx="405" cy="155" r="9" fill="#0f2a55"/><text x="405" y="175">2020</text><text x="405" y="100">Easy to edit</text><text x="405" y="107">with your text</text>
    </g>
    <circle cx="470" cy="155" r="19" fill="#9c1b1b"/>
    <text x="470" y="158" font-size="9" fill="#fff" text-anchor="middle" font-family="Open Sans" font-weight="700">2021</text>
    <text x="470" y="126" font-size="8" fill="#9c1b1b" text-anchor="middle" font-family="Open Sans" font-weight="700">Vision</text>
  </svg>
  <p class="foot">© Copyright Summit Lane Advisors | All Rights Reserved</p><p class="page">PAGE | 10</p>
</div>

<div class="slide" style="left:30px;top:2896px">
  <div class="bar"></div><h2 class="s-title">Your Title Here</h2><p class="s-sub">Subtitle Goes Here</p><span class="mark">SLA</span>
  <svg style="position:absolute;left:0;top:0" width="553" height="311" viewBox="0 0 553 311">
    <circle cx="80" cy="165" r="50" fill="#1f4f8f"/>
    <path d="M80 165 L30 165 A50 50 0 0 1 80 115 Z" fill="#dfe6f0"/>
    <text x="76" y="180" font-size="34" fill="#fff" text-anchor="middle" font-family="Libre Baskerville">75</text>
    <text x="110" y="160" font-size="13" fill="#fff" font-family="Libre Baskerville">%</text>
    <g font-family="Open Sans" font-size="4.5" fill="#8a9099" text-anchor="middle">
      <line x1="150" y1="250" x2="530" y2="250" stroke="#dfe3e8"/>
      <rect x="160" y="140" width="14" height="110" fill="#1f4f8f"/><text x="167" y="136">4.3</text><text x="167" y="258">Category 1</text>
      <rect x="225" y="190" width="14" height="60" fill="#1f4f8f"/><text x="232" y="186">2.5</text><text x="232" y="258">Category 2</text>
      <rect x="290" y="166" width="14" height="84" fill="#1f4f8f"/><text x="297" y="162">3.5</text><text x="297" y="258">Category 3</text>
      <rect x="355" y="136" width="14" height="114" fill="#1f4f8f"/><text x="362" y="132">4.5</text><text x="362" y="258">Category 4</text>
      <rect x="420" y="190" width="14" height="60" fill="#1f4f8f"/><text x="427" y="186">2.5</text><text x="427" y="258">Category 5</text>
      <rect x="485" y="210" width="14" height="40" fill="#9c1b1b"/><text x="492" y="206">1.6</text><text x="492" y="258">Category 6</text>
    </g>
  </svg>
  <div style="position:absolute;left:150px;top:70px;width:370px"><p class="h-small">Content Title Here</p><p class="txt">A clean, modern layout that is easy to edit with your own colours, photos and text for any topic.</p></div>
  <p class="foot">© Copyright Summit Lane Advisors | All Rights Reserved</p><p class="page">PAGE | 11</p>
</div>

<div class="slide" style="left:617px;top:2896px">
  <div class="bar"></div><h2 class="s-title">Your Title Here</h2><p class="s-sub">Subtitle Goes Here</p><span class="mark">SLA</span>
  <div class="ph" role="img" aria-label="Photo of an empty conference room" style="left:22px;top:62px;width:160px;height:85px;background:linear-gradient(180deg,#7d93b3,#3e5f8e)"><p class="serif" style="position:absolute;left:40px;bottom:8px;font-size:7px;color:#fff">Your Text Here</p></div>
  <div style="position:absolute;left:210px;top:68px;width:320px"><p class="h-small">Content Title Here</p><p class="txt">A clean, modern layout that is easy to edit with your own colours, photos and text. Easy to edit with your own colours and photos.</p></div>
  <div style="position:absolute;left:22px;top:170px;width:300px"><p class="h-small">Content Title Here</p><p class="txt">A clean, modern layout that is easy to edit with your own colours, photos and text. Easy to edit with your own colours and photos.</p></div>
  <div class="ph" role="img" aria-label="Photo of a hand signing a document with a pen" style="left:350px;top:175px;width:180px;height:85px;background:linear-gradient(135deg,#e6ebf2,#9fb3cf 70%,#3e66a0)"><p class="serif" style="position:absolute;left:50px;bottom:8px;font-size:7px;color:#fff">Your Text Here</p></div>
  <p class="foot">© Copyright Summit Lane Advisors | All Rights Reserved</p><p class="page">PAGE | 12</p>
</div>

<div class="slide" style="left:30px;top:3230px">
  <div class="bar"></div><h2 class="s-title">Your Title Here</h2><p class="s-sub">Subtitle Goes Here</p><span class="mark">SLA</span>
  <div class="ph" role="img" aria-label="City skyline at dusk with glowing network connections" style="left:22px;top:62px;width:250px;height:150px;background:linear-gradient(180deg,#8fa3bd,#3c5677 60%,#1e2f47);border-radius:4px"></div>
  <div style="position:absolute;left:30px;top:190px;background:var(--white);border-radius:9px;padding:3px 10px 3px 4px;font-size:5px;display:flex;align-items:center;gap:4px;color:var(--navy)"><span style="width:9px;height:9px;border-radius:50%;background:var(--navy);display:block"></span>Content Title Here</div>
  <div style="position:absolute;left:258px;top:85px;width:28px;height:28px;border-radius:50%;background:var(--navy)"></div>
  <div style="position:absolute;left:258px;top:150px;width:28px;height:28px;border-radius:50%;background:var(--red)"></div>
  <div style="position:absolute;left:300px;top:82px;width:230px"><p class="h-small">Content Title Here</p><p class="txt">A clean, modern layout that is easy to edit with your own colours, photos and text.</p></div>
  <div style="position:absolute;left:300px;top:147px;width:230px"><p class="h-small" style="color:var(--red)">Content Title Here</p><p class="txt">A clean, modern layout that is easy to edit with your own colours, photos and text.</p></div>
  <p class="foot">© Copyright Summit Lane Advisors | All Rights Reserved</p><p class="page">PAGE | 13</p>
</div>

<div class="slide" style="left:617px;top:3230px">
  <div class="bar"></div><h2 class="s-title">Pie Charts</h2><p class="s-sub">SUBTITLE GOES HERE</p><span class="mark">SLA</span>
  <p class="txt" style="position:absolute;left:90px;top:62px;width:370px;text-align:center">A clean, modern layout that is easy to edit with your own colours, photos and text. Simply impress your audience and add a unique touch.</p>
  <svg style="position:absolute;left:0;top:0" width="553" height="311" viewBox="0 0 553 311">
    <g fill="none" stroke-width="8">
      <circle cx="140" cy="150" r="30" stroke="#e3e7ec"/>
      <circle cx="140" cy="150" r="30" stroke="#1f5aa6" stroke-dasharray="128.2 188.5" transform="rotate(-90 140 150)"/>
      <circle cx="276" cy="150" r="30" stroke="#e3e7ec"/>
      <circle cx="276" cy="150" r="30" stroke="#9c1b1b" stroke-dasharray="66 188.5" transform="rotate(-90 276 150)"/>
      <circle cx="412" cy="150" r="30" stroke="#e3e7ec"/>
      <circle cx="412" cy="150" r="30" stroke="#7a7f87" stroke-dasharray="103.7 188.5" transform="rotate(-90 412 150)"/>
    </g>
    <g font-family="Libre Baskerville" font-size="13" fill="#3a3f47" text-anchor="middle">
      <text x="140" y="155">68%</text><text x="276" y="155">35%</text><text x="412" y="155">55%</text>
    </g>
  </svg>
  <p class="txt" style="position:absolute;left:100px;top:200px;width:80px;text-align:center">Easy to edit with your own colours and photos.</p>
  <p class="txt" style="position:absolute;left:236px;top:200px;width:80px;text-align:center">Easy to edit with your own colours and photos.</p>
  <p class="txt" style="position:absolute;left:372px;top:200px;width:80px;text-align:center">Easy to edit with your own colours and photos.</p>
  <p class="foot">© Northfield Studio LLC | All Rights Reserved</p><p class="page">PAGE | 14</p>
</div>

<div class="slide" style="left:30px;top:3564px">
  <div class="ph" role="img" aria-label="Photo of a person writing notes at a desk" style="left:0;top:0;width:265px;height:160px;background:linear-gradient(135deg,#d7dbe0,#9aa3ae 60%,#4a5563)"></div>
  <div style="position:absolute;left:0;top:160px;width:265px;height:151px;background:var(--navy)"></div>
  <div style="position:absolute;left:22px;top:147px;width:26px;height:26px;border-radius:50%;background:var(--blue);color:#fff;font:700 18px 'Libre Baskerville',serif;text-align:center;line-height:30px">”</div>
  <div style="position:absolute;left:22px;top:185px;width:220px"><p class="txt" style="color:#dbe4f2">A clean, modern layout that is easy to edit with your own colours, photos and text. Simply impress your audience and add a unique touch.</p><p style="font-size:5px;color:#fff;margin-top:6px">- Name Here</p></div>
  <span class="mark">SLA</span>
  <h2 class="s-title" style="left:290px;top:62px">Your Title Here</h2>
  <p class="txt" style="position:absolute;left:290px;top:88px;width:240px">A clean, modern layout that is easy to edit with your own colours, photos and text for any topic you need.</p>
  <div style="position:absolute;left:290px;top:140px;width:240px">
    <div style="display:flex;gap:6px;margin-bottom:8px"><span style="width:7px;height:7px;border-radius:50%;background:var(--navy);flex:none;margin-top:1px"></span><p class="txt">Easy to edit with your own colours and photos.</p></div>
    <div style="display:flex;gap:6px;margin-bottom:8px"><span style="width:7px;height:7px;border-radius:50%;background:var(--red);flex:none;margin-top:1px"></span><p class="txt">Easy to edit with your own colours and photos.</p></div>
    <div style="display:flex;gap:6px;margin-bottom:8px"><span style="width:7px;height:7px;border-radius:50%;background:var(--navy);flex:none;margin-top:1px"></span><p class="txt">Easy to edit with your own colours and photos.</p></div>
    <div style="display:flex;gap:6px"><span style="width:7px;height:7px;border-radius:50%;background:var(--grey);flex:none;margin-top:1px"></span><p class="txt">Easy to edit with your own colours and photos.</p></div>
  </div>
  <p class="foot" style="color:#c9d6ea">© Copyright Summit Lane Advisors | All Rights Reserved</p><p class="page">PAGE | 15</p>
</div>

<div class="slide navy" style="left:617px;top:3564px">
  <div class="ghost" style="left:10px;top:70px;color:rgba(255,255,255,.05)">SLA</div>
  <div style="position:absolute;left:330px;top:45px;width:200px;text-align:center">
    <p style="font:800 28px 'Open Sans',Arial,sans-serif;line-height:1">SLA</p>
    <p style="font-weight:700;font-size:10px;margin-top:3px">Summit Lane Advisors</p>
    <p style="font-size:5.5px;letter-spacing:1.5px">Clear advice, lasting results</p>
  </div>
  <div style="position:absolute;left:350px;top:195px;width:20px;height:1.5px;background:#fff"></div>
  <p class="serif" style="position:absolute;left:350px;top:203px;font-size:16px">Section Title</p>
  <p class="txt" style="position:absolute;left:350px;top:228px;width:170px">A clean, modern layout that is easy to edit with your own colours, photos and text.</p>
</div>

<div class="slide" style="left:30px;top:3899px">
  <div class="ghost" style="left:10px;top:70px">SLA</div>
  <div style="position:absolute;left:190px;top:30px;width:200px;text-align:center">
    <p style="font:800 28px 'Open Sans',Arial,sans-serif;line-height:1;color:var(--navy)">SLA</p>
    <p style="font-weight:700;font-size:10px;margin-top:3px;color:var(--navy)">Summit Lane Advisors</p>
    <p style="font-size:5.5px;letter-spacing:1.5px;color:var(--blue)">Clear advice, lasting results</p>
  </div>
  <div style="position:absolute;left:350px;top:195px;width:20px;height:1.5px;background:var(--navy)"></div>
  <p class="serif" style="position:absolute;left:350px;top:203px;font-size:16px;color:var(--navy)">Section Title</p>
  <p class="txt" style="position:absolute;left:350px;top:228px;width:170px">A clean, modern layout that is easy to edit with your own colours, photos and text.</p>
</div>

<div class="slide" style="left:617px;top:3899px">
  <div class="bar"></div><h2 class="s-title">Your Title Here</h2><p class="s-sub">SUBTITLE GOES HERE</p><span class="mark">SLA</span>
  <div class="member" style="left:42px"><div class="photo" role="img" aria-label="Portrait photo of a team member" style="background:linear-gradient(180deg,#d9cbbd,#8a7563)"></div><p class="name">Member Name</p><p class="txt">Easy to edit with your own text.</p><div class="socials"><i></i><i></i><i></i><i></i></div></div>
  <div class="member" style="left:160px"><div class="photo" role="img" aria-label="Portrait photo of a team member" style="background:linear-gradient(180deg,#c7443e,#6e2a2a)"></div><p class="name">Member Name</p><p class="txt">Easy to edit with your own text.</p><div class="socials"><i></i><i></i><i></i><i></i></div></div>
  <div class="member" style="left:278px"><div class="photo" role="img" aria-label="Portrait photo of a team member" style="background:linear-gradient(180deg,#e8e8e8,#6b5b52)"></div><p class="name">Member Name</p><p class="txt">Easy to edit with your own text.</p><div class="socials"><i></i><i></i><i></i><i></i></div></div>
  <div class="member" style="left:396px"><div class="photo" role="img" aria-label="Portrait photo of a team member" style="background:linear-gradient(180deg,#9aa0a8,#2b2f36)"></div><p class="name">Member Name</p><p class="txt">Easy to edit with your own text.</p><div class="socials"><i></i><i></i><i></i><i></i></div></div>
  <p class="page">PAGE | 18</p>
</div>

<div class="slide" style="left:30px;top:4233px">
  <div class="bar"></div><h2 class="s-title">Editable Icons</h2><span class="mark">SLA</span>
  <div class="ph" role="img" aria-label="Grid of editable blue line icons for business topics" style="left:22px;top:55px;width:509px;height:225px;background:linear-gradient(180deg,#e3eaf4,#c9d6e8)"></div>
  <p class="page">PAGE | 19</p>
</div>

<div class="slide" style="left:617px;top:4233px">
  <div class="bar"></div><h2 class="s-title">Contact Us</h2>
  <div class="ghost" style="left:240px;top:90px;font-size:150px">SLA</div>
  <div class="ph" role="img" aria-label="Portrait photo of the presenter" style="left:45px;top:60px;width:55px;height:55px;border-radius:50%;background:linear-gradient(180deg,#d3d6da,#5d646e)"></div>
  <p style="position:absolute;left:40px;top:125px;border:1px solid var(--rule);border-radius:8px;padding:3px 14px;font:400 5.5px 'Libre Baskerville',serif;letter-spacing:1.5px;color:var(--navy)">PRESENTER NAME</p>
  <div style="position:absolute;left:45px;top:155px">
    <div class="contact-row"><svg width="8" height="8" viewBox="0 0 10 10"><path d="M2 1l2 2-1 1.5c.6 1.2 1.3 1.9 2.5 2.5L7 6l2 2-1.5 1.5C4 9 1 6 .5 2.5z" fill="#0f3a78"/></svg>+46 8 555 0142</div>
    <div class="contact-row"><svg width="8" height="8" viewBox="0 0 10 10"><circle cx="5" cy="5" r="4" fill="none" stroke="#0f3a78"/><path d="M1 5h8M5 1c-2 2.5-2 5.5 0 8M5 1c2 2.5 2 5.5 0 8" fill="none" stroke="#0f3a78" stroke-width=".7"/></svg>www.summitlaneadvisors.se</div>
    <div class="contact-row"><svg width="8" height="8" viewBox="0 0 10 10"><rect x="1" y="2" width="8" height="6" fill="none" stroke="#0f3a78"/><path d="M1 2l4 3.5L9 2" fill="none" stroke="#0f3a78"/></svg>hello@summitlaneadvisors.se</div>
    <div class="contact-row"><svg width="8" height="8" viewBox="0 0 10 10"><path d="M5 9.5C2.5 6.5 1.5 5 1.5 3.5a3.5 3.5 0 017 0C8.5 5 7.5 6.5 5 9.5z" fill="#0f3a78"/><circle cx="5" cy="3.5" r="1.2" fill="#fff"/></svg>Add your location here</div>
  </div>
  <div style="position:absolute;left:300px;top:140px;width:200px;text-align:center">
    <p style="font:800 34px 'Open Sans',Arial,sans-serif;line-height:1;color:var(--navy)">SLA</p>
    <p style="font-weight:700;font-size:11px;margin-top:3px;color:var(--navy)">Summit Lane Advisors</p>
    <p style="font-size:6px;letter-spacing:1.5px;color:var(--blue)">Clear advice, lasting results</p>
  </div>
  <p class="foot">© Copyright Summit Lane Advisors | All Rights Reserved</p>
</div>

</body>
</html>
```